Logo and Flyer for Co-Branded Comedy Show

Graphic designer needed to create a promotional flyer for a comedy show. Two different comedy shows, with distinct branding, are joining forces to create a combined show. (co-branded logo to be included is attached.)

The design of the promotional materials should be a modern take on a vintage poster a la Quirkwood Jamboree. We'd like it to be a vintage look with a modern twist (I have attached the Quirkwood Jamboree Flyer for reference - marked up with info for our show) Filename: PLGRVN Flyer Mark Up

Images of the two hosts are attached: Filenames:

Our show will be in a theater, so if it can play off a playbill that would be great. I have attached examples of the clean look that we like, as well as some vintage theater flyers. We'd like to stay on the lighter side of the color palette (light gray, blues, etc. which is in line with the Harbor Laughs Live flyer) Filename: PLGR VN Flyer Direction

Current Branding of the individual Shows
I have attached the current promo materials for the individual shows, so you have a sense of the color palette and logo treatment.

The deliverable:
1 flyer vertical, 1 flyer horizontal - same design/concept but in 2 orientation (vertical and horizontal) horizontal will be used for web.
***This flyer will include the co-branded logo seen attached - Harbor Laughs Live Gets Real Honest (individual logos already created and attached) - Download PSD File here: http://lnk.example-short.test/PLGRVN

Industry/Entity Type

Graphic Designer

Colors
0493cd
85cae6
ecf7fb
f5f5f5
ffffff
606060
fbfbfb
0255a3
3176b5

Requirements
Must have
• Vintage look with a modern twist
• Vertical and horizontal options

```html
<!DOCTYPE html>
<html lang="en">
<head>
<meta charset="utf-8">
<title>Harbor Laughs Live – Gets Real Honest Comedy Show</title>
<link rel="stylesheet" href="https://fonts.googleapis.com/css2?family=Montserrat:wght@600;700;800&family=Oswald:wght@400;500;600;700&family=Rye&family=Open+Sans:wght@400;600&display=swap">
<style>
  :root {
    --backdrop: #5b5f67;
    --paper: #f4f4f4;
    --ink: #4a4a4a;
    --ink-dark: #2b2b2b;
    --blue: #1f5fc4;
    --navy: #1d4f7c;
    --navy-band: #1e4b74;
    --white: #ffffff;
  }
  * { box-sizing: border-box; margin: 0; padding: 0; }
  html, body { width: 1200px; height: 1000px; overflow: hidden; }
  body { background: var(--backdrop); font-family: "Open Sans", sans-serif; }

  .flyer {
    position: absolute; left: 288px; top: 18px; width: 620px; height: 960px;
    background: var(--paper); color: var(--ink); overflow: hidden;
  }
  .abs { position: absolute; left: 0; width: 100%; text-align: center; }
  .dots { position: absolute; border-top: 3px dotted #555; }

  .producer {
    top: 36px; font-family: "Montserrat", sans-serif; font-weight: 800;
    font-size: 20px; letter-spacing: 1px; color: var(--ink-dark); line-height: 1;
  }
  .producer small { display: block; font-size: 10px; letter-spacing: 2px; margin-top: 3px; }

  .presents { top: 82px; font-family: "Montserrat", sans-serif; font-weight: 700; font-size: 16px; line-height: 1; color: var(--blue); }
  .show-brand {
    top: 104px; font-family: "Montserrat", sans-serif; font-weight: 800;
    font-size: 40px; line-height: 1; color: var(--blue);
  }
  .brand-rule { position: absolute; left: 210px; top: 156px; width: 200px; height: 6px; background: var(--blue); }

  .title {
    top: 212px; font-family: "Montserrat", sans-serif; font-weight: 800;
    font-size: 64px; line-height: 0.95; color: var(--ink); letter-spacing: -1px;
  }
  .subtitle {
    top: 352px; font-family: "Rye", serif; font-size: 36px; line-height: 1; color: #555; letter-spacing: 1px;
  }

  .portrait { position: absolute; }
  .portrait svg { position: absolute; left: 0; display: block; }
  .role {
    position: absolute; left: 0; width: 100%; text-align: center;
    font-family: "Oswald", sans-serif; font-size: 13px; line-height: 1; color: var(--ink-dark);
  }
  .host-name {
    position: absolute; left: 0; width: 100%; text-align: center;
    font-family: "Rye", serif; font-size: 15px; line-height: 1.1; color: var(--ink-dark);
  }
  .host-credit {
    position: absolute; left: -10px; width: calc(100% + 20px); text-align: center;
    font-family: "Oswald", sans-serif; font-size: 9.5px; line-height: 1.1; color: var(--ink-dark);
  }
  .featured-label { position: absolute; left: 0; width: 100%; text-align: center; }
  .featured-label .lead { font-family: "Oswald", sans-serif; font-size: 14px; line-height: 1; color: var(--ink-dark); }
  .featured-label .name { font-family: "Rye", serif; font-size: 42px; line-height: 1; color: var(--ink-dark); margin-top: 2px; }

  .one-night { top: 692px; font-family: "Oswald", sans-serif; font-weight: 600; font-size: 24px; line-height: 1; color: var(--ink-dark); }
  .date {
    top: 722px; font-family: "Oswald", sans-serif; font-weight: 600; font-size: 50px;
    line-height: 1; color: var(--ink);
  }
  .featuring-row { position: absolute; left: 26px; top: 784px; width: 594px; height: 20px; }
  .featuring-row em { font-family: "Oswald", sans-serif; font-style: normal; font-size: 18px; line-height: 1; color: var(--navy); position: absolute; left: 0; top: -2px; }
  .featuring-row .bar { position: absolute; left: 92px; right: 0; top: 4px; height: 11px; background: var(--navy); }

  .lineup {
    position: absolute; left: 26px; top: 806px; width: 570px;
    display: flex; justify-content: space-between; align-items: center;
    font-family: "Oswald", sans-serif; font-weight: 600; font-size: 19px; line-height: 1.05;
    color: var(--navy); text-align: center; text-transform: uppercase;
  }
  .venue {
    position: absolute; left: 0; top: 852px; width: 100%; height: 30px;
    background: var(--navy-band); box-shadow: 0 -4px 0 -1px var(--white), 0 -5px 0 -1px var(--navy-band);
    color: var(--white); font-family: "Oswald", sans-serif; font-size: 20px; line-height: 30px; text-align: center;
  }
  .tickets { top: 902px; font-family: "Oswald", sans-serif; font-size: 11px; line-height: 1; color: #666; }
  .site { top: 914px; font-family: "Oswald", sans-serif; font-size: 20px; line-height: 1.1; color: #555; }
  .site b { font-weight: 600; color: var(--ink-dark); }
</style>
</head>
<body>
<main class="flyer">
  <div class="dots" style="left:30px; top:44px; width:160px;"></div>
  <div class="dots" style="left:430px; top:44px; width:160px;"></div>
  <div class="abs producer">PALELINE<small>ENTERTAINMENT</small></div>

  <div class="abs presents">presents</div>
  <div class="abs show-brand">Harbor Laughs Live</div>
  <div class="brand-rule"></div>

  <h1 class="abs title">GETS REAL<br>HONEST</h1>
  <div class="abs subtitle">Comedy Show</div>

  <!-- Left co-host -->
  <div class="portrait" style="left:36px; top:446px; width:128px; height:230px;">
    <div class="role" style="top:0;">CO-HOST</div>
    <svg style="top:18px;" width="128" height="148" viewBox="0 0 128 148" role="img" aria-label="Portrait photo of co-host Zolo Brightwave">
      <defs><linearGradient id="photoLeft" x1="0" y1="0" x2="0" y2="1"><stop offset="0" stop-color="#d9d9d9"/><stop offset="1" stop-color="#3a3d44"/></linearGradient></defs>
      <ellipse cx="64" cy="74" rx="60" ry="71" fill="url(#photoLeft)" stroke="#222" stroke-width="4"/>
    </svg>
    <div class="host-name" style="top:172px;">ZOLO<br>BRIGHTWAVE</div>
    <div class="host-credit" style="top:208px;">(Late Loop, Wave 88)</div>
  </div>

  <!-- Featured -->
  <div class="portrait" style="left:172px; top:438px; width:276px; height:240px;">
    <svg style="top:0;" width="276" height="170" viewBox="0 0 276 170" role="img" aria-label="Portrait photo of featured comedian Dashiell">
      <defs><linearGradient id="photoMain" x1="0" y1="0" x2="0" y2="1"><stop offset="0" stop-color="#f0f0f0"/><stop offset="0.5" stop-color="#6d6257"/><stop offset="1" stop-color="#2f3137"/></linearGradient></defs>
      <ellipse cx="138" cy="85" rx="134" ry="81" fill="url(#photoMain)" stroke="#222" stroke-width="4"/>
    </svg>
    <div class="featured-label" style="top:178px;">
      <div class="lead">FEATURING</div>
      <div class="name">DASHIELL</div>
    </div>
  </div>

  <!-- Right co-host -->
  <div class="portrait" style="left:456px; top:446px; width:128px; height:230px;">
    <div class="role" style="top:0;">CO-HOST</div>
    <svg style="top:18px;" width="128" height="148" viewBox="0 0 128 148" role="img" aria-label="Portrait photo of co-host Marla Vintrow">
      <defs><linearGradient id="photoRight" x1="0" y1="0" x2="0" y2="1"><stop offset="0" stop-color="#cfcfcf"/><stop offset="1" stop-color="#2f4a4a"/></linearGradient></defs>
      <ellipse cx="64" cy="74" rx="60" ry="71" fill="url(#photoRight)" stroke="#222" stroke-width="4"/>
    </svg>
    <div class="host-name" style="top:172px;">MARLA<br>VINTROW</div>
    <div class="host-credit" style="top:208px;">(Laugh Channel, City Comedy Fest)</div>
  </div>

  <div class="dots" style="left:26px; top:698px; width:170px;"></div>
  <div class="dots" style="left:26px; top:706px; width:170px;"></div>
  <div class="dots" style="left:424px; top:698px; width:170px;"></div>
  <div class="dots" style="left:424px; top:706px; width:170px;"></div>
  <div class="abs one-night">ONE NIGHT ONLY</div>
  <div class="abs date">SATURDAY, AUGUST 22, 2015</div>

  <div class="featuring-row"><em>featuring</em><div class="bar"></div></div>
  <div class="lineup">
    <span>Theo<br>Larkin</span>
    <span>Ellis<br>Feldgrove</span>
    <span>Rowan<br>Pellick</span>
    <span>Nadia<br>Volkren</span>
    <span>Dashiell</span>
    <span>Simon<br>Carvell</span>
  </div>

  <div class="venue">Meridian Hall | 214 Quayside Ave, Harborview, NY 10000</div>

  <div class="abs tickets">For Tickets and More Information Please Visit</div>
  <div class="abs site">www.<b>PLGRVN</b>.com</div>
</main>
</body>
</html>
```